Velvet Pressings Techno Label Business Card

I'm looking for a very clean business card for my Velvet Pressings music label. The label focusses on techno music. The card should include:

• my name : Daniel Hovind as "Founder & CEO"
• email address: daniel@velvet-pressings.net
• web: www.velvet-pressings.net
• facebook logo + /velvetprs
• twitter logo + /velvetprs
• soundcloud logo + /velvetpressings

Feel free to include your ideas! I'm looking forward to discuss about it.

Daniel

Industry/Entity Type

Business

Contact Information for Business Card

I don't like glossy cards. Prefer matt.

Requirements
Nice to have
• Maybe on one side the complete logo, other side just the icon.
Should not have
• Flashy stuff. Must be clean and business like style.

```html
<!DOCTYPE html>
<html lang="en">
<head>
<meta charset="utf-8">
<title>Velvet Pressings – Business Card</title>
<link rel="stylesheet" href="https://fonts.googleapis.com/css2?family=Open+Sans:wght@400;600;700&display=swap">
<style>
  :root {
    --page-bg: #e6e4e1;
    --card-black: #151515;
    --brand-orange: #f26a21;
    --text-grey: #8a8a8a;
    --line-grey: #9a9a9a;
    --contact-white: #e9e9e9;
    --divider: #2c2c2c;
  }
  * { box-sizing: border-box; margin: 0; padding: 0; }
  html, body {
    width: 1200px; height: 1000px; overflow: hidden;
    background: var(--page-bg);
    font-family: "Open Sans", Arial, sans-serif;
  }
  .canvas { position: relative; width: 1200px; height: 1000px; }

  .card {
    position: absolute; width: 700px; height: 400px;
    background: var(--card-black);
    overflow: hidden;
    box-shadow: 0 6px 18px rgba(0,0,0,0.18);
  }
  .card-front { left: 70px; top: 70px; }
  .card-back  { left: 430px; top: 530px; }

  /* Front side */
  .front-mark {
    position: absolute; left: 150px; top: 155px;
    width: 90px; height: 90px; border-radius: 50%;
    background: var(--brand-orange);
  }
  .front-name {
    position: absolute; left: 272px; top: 172px;
    font-size: 40px; font-weight: 700; letter-spacing: -0.5px;
    color: var(--brand-orange); line-height: 56px;
  }

  /* Back side */
  .back-band { position: absolute; inset: 0; width: 700px; height: 400px; }
  .back-logo {
    position: absolute; left: 150px; top: 70px;
    display: flex; align-items: center; gap: 14px;
  }
  .back-logo-mark {
    width: 40px; height: 40px; border-radius: 50%;
    background: var(--brand-orange);
  }
  .back-logo-name {
    font-size: 30px; font-weight: 700; letter-spacing: -0.4px;
    color: var(--brand-orange);
  }
  .holder { position: absolute; left: 300px; top: 250px; }
  .holder-name {
    font-size: 22px; font-weight: 600; color: var(--brand-orange); line-height: 28px;
  }
  .holder-role { font-size: 15px; color: var(--text-grey); line-height: 22px; }

  .divider { position: absolute; left: 0; top: 0; width: 700px; height: 400px; }

  .contacts {
    position: absolute; left: 455px; top: 120px;
    list-style: none; display: flex; flex-direction: column; gap: 9px;
  }
  .contact-row { display: flex; align-items: center; gap: 16px; }
  .contact-item { display: flex; align-items: center; gap: 8px; }
  .contact-icon {
    width: 20px; height: 20px; background: var(--brand-orange);
    border-radius: 2px; flex: none;
    display: flex; align-items: center; justify-content: center;
  }
  .contact-text { font-size: 13px; color: var(--contact-white); }
</style>
</head>
<body>
<main class="canvas">

  <section class="card card-front" aria-label="Business card front">
    <div class="front-mark"></div>
    <div class="front-name">Velvet Pressings</div>
  </section>

  <section class="card card-back" aria-label="Business card back">
    <svg class="back-band" viewBox="0 0 700 400" aria-hidden="true">
      <path d="M0,0 L40,0 C90,160 250,330 430,400 L0,400 Z" fill="var(--brand-orange)"/>
      <path d="M48,0 C98,158 258,328 442,400" fill="none" stroke="var(--line-grey)" stroke-width="4"/>
    </svg>

    <div class="back-logo">
      <span class="back-logo-mark"></span>
      <span class="back-logo-name">Velvet Pressings</span>
    </div>

    <div class="holder">
      <div class="holder-name">Daniel Hovind</div>
      <div class="holder-role">Founder &amp; CEO</div>
    </div>

    <svg class="divider" viewBox="0 0 700 400" aria-hidden="true">
      <line x1="430" y1="118" x2="470" y2="262" stroke="var(--divider)" stroke-width="1.5"/>
    </svg>

    <ul class="contacts">
      <li class="contact-row">
        <span class="contact-item">
          <span class="contact-icon">
            <svg width="14" height="10" viewBox="0 0 14 10" aria-hidden="true">
              <rect x="0.5" y="0.5" width="13" height="9" fill="none" stroke="var(--card-black)" stroke-width="1.3"/>
              <path d="M0.5,0.5 L7,5.5 L13.5,0.5" fill="none" stroke="var(--card-black)" stroke-width="1.3"/>
            </svg>
          </span>
          <span class="contact-text">daniel@velvet-pressings.net</span>
        </span>
      </li>
      <li class="contact-row">
        <span class="contact-item">
          <span class="contact-icon">
            <svg width="14" height="14" viewBox="0 0 14 14" aria-hidden="true">
              <circle cx="7" cy="7" r="6" fill="none" stroke="var(--card-black)" stroke-width="1.3"/>
              <ellipse cx="7" cy="7" rx="2.6" ry="6" fill="none" stroke="var(--card-black)" stroke-width="1.1"/>
              <line x1="1" y1="7" x2="13" y2="7" stroke="var(--card-black)" stroke-width="1.1"/>
            </svg>
          </span>
          <span class="contact-text">www.velvet-pressings.net</span>
        </span>
      </li>
      <li class="contact-row">
        <span class="contact-item">
          <span class="contact-icon"></span>
          <span class="contact-text">/velvetprs</span>
        </span>
        <span class="contact-item">
          <span class="contact-icon"></span>
          <span class="contact-text">/velvetprs</span>
        </span>
      </li>
      <li class="contact-row">
        <span class="contact-item">
          <span class="contact-icon"></span>
          <span class="contact-text">/velvetpressings</span>
        </span>
      </li>
    </ul>
  </section>

</main>
</body>
</html>
```